Business Card & Email Signature Design || Upmarket + Luxury

Riverlume Honey, a New Zealand Manuka Honey company needs a Business Card & Email Signature design.

Our logo's are attached in Gold & Black versions, feel free to be creative with how you use the logo and it's patterns in your design.

Style:
- Looking for an Elegant, Luxurious, Upmarket feel.
- Black/Matte Black Card, Gold Foil, UV Embossing

Information to Add:

- Logo
- Company Name: Riverlume Honey
- Name: Mattias Brovell
- Title: Creative Director
- Phone: +64 2919 58 617
- Email: mattias@riverlumehoney.example
- Website: www.riverlumehoney.example

- Socials: ***For email Signature Only***
- Facebook: https://www.facebook.com/riverlumehoney/
- Instagram: https://www.instagram.com/riverlumehoney/

Target Market(s)

Asia/Europe Luxury, Upmarket

Contact Information for Business Card

- Logo
- Name: Mattias Brovell
- Phone: +64 2919 58 617

Font styles to use
Other font styles liked:
• Champagne & Limousines (Attached)

Requirements
Must have
• Business Card & Email Signature Design.

Looking for a Sleek, Luxury, Upmarket Design.

```html
<!DOCTYPE html>
<html lang="en">
<head>
<meta charset="utf-8">
<title>Riverlume Honey — Business Card</title>
<link rel="stylesheet" href="https://fonts.googleapis.com/css2?family=Josefin+Sans:wght@300;400&display=swap">
<style>
  :root {
    --backdrop: #1a1a1a;
    --card: #121416;
    --card-edge: #1b1d20;
    --gold: #c9a45a;
    --gold-soft: rgba(201, 164, 90, 0.22);
    --ivory: #ece6d8;
    --text-font: "Josefin Sans", sans-serif;
  }
  * { box-sizing: border-box; margin: 0; padding: 0; }
  html, body {
    width: 1200px; height: 675px; overflow: hidden;
    background: var(--backdrop);
    font-family: var(--text-font);
  }
  .stage {
    position: relative; width: 1200px; height: 675px;
    display: flex; align-items: center; justify-content: center; gap: 40px;
  }
  .card {
    position: relative; width: 520px; height: 300px;
    background: linear-gradient(160deg, var(--card-edge), var(--card) 60%);
    overflow: hidden;
    box-shadow: 0 18px 40px rgba(0,0,0,0.45);
  }
  .card__pattern {
    position: absolute; width: 300px; height: 200px;
  }
  .card--front .card__pattern {
    top: 0; left: 0;
    background: radial-gradient(ellipse at 15% 20%, var(--gold-soft), rgba(60,58,54,0.25) 45%, transparent 75%);
  }
  .card--back .card__pattern {
    top: 0; right: 0;
    background: radial-gradient(ellipse at 80% 25%, var(--gold-soft), rgba(60,58,54,0.25) 45%, transparent 75%);
  }
  .brand {
    position: absolute; top: 96px; left: 0; right: 0;
    display: flex; flex-direction: column; align-items: center; gap: 22px;
  }
  .brand__mark {
    width: 54px; height: 54px; border-radius: 50%;
    border: 1.5px solid var(--gold);
  }
  .brand__name {
    color: var(--gold); font-weight: 400; font-size: 38px;
    letter-spacing: 0.16em; text-transform: uppercase;
  }
  .website {
    position: absolute; bottom: 30px; left: 0; right: 0;
    text-align: center; color: var(--ivory);
    font-size: 17px; font-weight: 400; letter-spacing: 0.02em;
  }
  .contact {
    position: absolute; left: 52px; top: 128px;
  }
  .contact__title {
    display: inline-block; color: var(--gold);
    font-size: 17px; font-weight: 300;
    padding-bottom: 3px; border-bottom: 1px solid var(--gold);
  }
  .contact__name {
    color: var(--ivory); font-size: 40px; font-weight: 400;
    text-transform: uppercase; margin-top: 10px; letter-spacing: 0.01em;
  }
  .contact__list { list-style: none; margin-top: 14px; }
  .contact__item {
    display: flex; align-items: center; gap: 12px;
    color: var(--ivory); font-size: 17px; font-weight: 400; margin-top: 6px;
  }
  .contact__label { font-weight: 300; color: #d9d3c5; }
  .contact__icon { width: 20px; height: 18px; flex: none; }
</style>
</head>
<body>
<main class="stage">
  <section class="card card--front">
    <div class="card__pattern" role="img" aria-label="Gold honeycomb line pattern fading from the top-left corner"></div>
    <div class="brand">
      <span class="brand__mark"></span>
      <span class="brand__name">Riverlume Honey</span>
    </div>
    <p class="website">www.riverlumehoney.example</p>
  </section>

  <section class="card card--back">
    <div class="card__pattern" role="img" aria-label="Gold honeycomb line pattern fading from the top-right corner"></div>
    <div class="contact">
      <span class="contact__title">Creative Director</span>
      <h1 class="contact__name">Mattias Brovell</h1>
      <ul class="contact__list">
        <li class="contact__item">
          <svg class="contact__icon" viewBox="0 0 20 20" aria-hidden="true">
            <path d="M4 2 L7.5 2 L9 6.5 L7 8 C8 10.5 9.5 12 12 13 L13.5 11 L18 12.5 L18 16 C18 17 17 18 16 18 C8.5 17.5 2.5 11.5 2 4 C2 3 3 2 4 2 Z" fill="var(--gold)"/>
          </svg>
          <span><span class="contact__label">Phone:</span> +64 2919 58 617</span>
        </li>
        <li class="contact__item">
          <svg class="contact__icon" viewBox="0 0 22 16" aria-hidden="true">
            <rect x="1" y="1" width="20" height="14" fill="none" stroke="var(--gold)" stroke-width="1.6"/>
            <path d="M1 1 L11 9 L21 1 M1 15 L8 7 M21 15 L14 7" fill="none" stroke="var(--gold)" stroke-width="1.6"/>
          </svg>
          <span><span class="contact__label">Email:</span> mattias@riverlumehoney.example</span>
        </li>
      </ul>
    </div>
  </section>
</main>
</body>
</html>
```